Curriculum Card Design for Martial Arts System

We need an editable curriculum card design for a martial arts system. Would like to have our logo in background or highlighted on card. Each level will have their own separate card that can be printed onto a postcard sized paper (5x7 and 6x9). Each technique has three parts to it E, F, and S and would like them to be able to have a line or box which an instructor can initial or check next to each technique. Would like to have each curriculum card be straightforward with slight modern and futuristic touches similar to the emblem and logo.

Industry/Entity Type

Martial Art

Requirements
Must have
• Must be able to be edited as the curriculum techniques and moves may change or added/subracted.We are looking for something that is very easy to understand but also eye catching.
Should not have
• please Don't be boring in design.

```html
<!DOCTYPE html>
<html lang="en">
<head>
<meta charset="utf-8">
<title>Curriculum Card – Level One &amp; Two</title>
<link href="https://fonts.googleapis.com/css2?family=Passion+One:wght@400;700&family=Lato:wght@400;700&display=swap" rel="stylesheet">
<style>
  :root{
    --panel-dark:#0f1616;
    --panel-dark-2:#1b2424;
    --teal:#2e7f7e;
    --teal-light:#3a9593;
    --teal-deep:#226766;
    --accent:#39c6cf;
    --ink:#0c1414;
    --white:#f4f7f6;
    --ribbon:#3a1416;
    --ribbon-edge:#5a2226;
  }
  *{margin:0;padding:0;box-sizing:border-box}
  html,body{width:922px;height:1200px;overflow:hidden;background:#e9ecec}
  .card{position:relative;width:922px;height:1200px;font-family:"Lato",sans-serif;color:var(--white)}
  .side{position:absolute;left:0;top:0;width:333px;height:1200px;
    background:linear-gradient(180deg,var(--panel-dark) 0%,var(--panel-dark-2) 45%,var(--panel-dark) 100%)}
  .brand{position:absolute;left:32px;top:22px;width:251px;height:218px;border:4px solid #050909;
    display:flex;flex-direction:column;align-items:center;justify-content:center;gap:18px}
  .brand-dot{width:74px;height:74px;border-radius:50%;background:var(--accent)}
  .brand-name{font-family:"Lato",sans-serif;font-weight:700;font-size:21px;letter-spacing:2px;color:var(--accent);text-align:center;line-height:1.2}
  .select-label{position:absolute;left:32px;top:290px;font-weight:700;font-size:21px;color:var(--white)}
  .check-row{position:absolute;left:32px;display:flex;align-items:center}
  .check-row span{width:36px;font-size:22px;color:var(--accent)}
  .check-row i{display:block;width:122px;height:28px;border:1.5px solid var(--accent);opacity:.7}
  .athlete{position:absolute;left:42px;top:490px;width:275px;height:580px;
    background:radial-gradient(ellipse at 50% 50%,#050808 0%,#0b1212 55%,rgba(15,22,22,0) 75%)}
  .main{position:absolute;left:333px;top:0;width:589px;height:1200px;
    background:radial-gradient(ellipse at 40% 30%,var(--teal-light) 0%,var(--teal) 55%,var(--teal-deep) 100%)}
  .frame{position:absolute;inset:0;width:589px;height:1200px}
  .ornament{position:absolute;background:rgba(12,20,20,.45);border-radius:40px}
  .banner{position:absolute;left:142px;width:302px;height:50px}
  .banner svg{position:absolute;inset:0}
  .banner b{position:absolute;inset:0;display:flex;align-items:center;justify-content:center;
    font-family:"Passion One",sans-serif;font-weight:700;font-size:34px;color:var(--white);letter-spacing:1px}
  .group{position:absolute}
  .group h3{font-family:"Passion One",sans-serif;font-weight:400;font-size:28px;letter-spacing:.5px;
    color:var(--white);display:flex;align-items:center;gap:6px;line-height:1;margin-bottom:8px}
  .group h3 svg{width:18px;height:18px;fill:var(--white)}
  .group ul{list-style:none;padding-left:27px}
  .group li{font-size:19px;line-height:30px}
  .group li::before{content:"•";margin-right:6px}
  .group.ruled ul{border-left:2px solid var(--white);padding-left:12px;margin-left:15px}
</style>
</head>
<body>
<div class="card">
  <aside class="side">
    <div class="brand">
      <div class="brand-dot"></div>
      <div class="brand-name">VANTAGE<br>COMBAT ARTS</div>
    </div>
    <div class="select-label">SELECT</div>
    <div class="check-row" style="top:327px"><span>E</span><i></i></div>
    <div class="check-row" style="top:372px"><span>F</span><i></i></div>
    <div class="check-row" style="top:416px"><span>S</span><i></i></div>
    <div class="athlete" role="img" aria-label="Silhouette of a martial artist holding a high standing kick"></div>
  </aside>

  <main class="main">
    <svg class="frame" viewBox="0 0 589 1200">
      <line x1="29" y1="28" x2="565" y2="28" stroke="#0c1414" stroke-width="3"/>
      <line x1="565" y1="28" x2="565" y2="1178" stroke="#0c1414" stroke-width="3"/>
      <line x1="29" y1="1178" x2="565" y2="1178" stroke="#0c1414" stroke-width="3"/>
      <rect x="23" y="22" width="10" height="10" transform="rotate(45 28 27)" fill="#0c1414"/>
      <rect x="23" y="1172" width="10" height="10" transform="rotate(45 28 1177)" fill="#0c1414"/>
    </svg>
    <div class="ornament" style="left:512px;top:417px;width:77px;height:200px" role="img" aria-label="Dragon ornament climbing the frame"></div>
    <div class="ornament" style="left:330px;top:1040px;width:255px;height:150px;border-radius:60px 20px 20px 60px" role="img" aria-label="Curling vine ornament in the corner"></div>

    <div class="banner" style="top:40px">
      <svg viewBox="0 0 302 50" preserveAspectRatio="none"><polygon points="0,0 302,0 282,25 302,50 0,50 20,25" fill="var(--ribbon)"/><polyline points="22,6 280,6" stroke="var(--ribbon-edge)" stroke-dasharray="4 3" stroke-width="1.5"/><polyline points="22,44 280,44" stroke="#b98" stroke-dasharray="4 3" stroke-width="1.5"/></svg>
      <b>LEVEL ONE</b>
    </div>

    <section class="group" style="left:24px;top:118px">
      <h3><svg viewBox="0 0 20 20"><circle cx="12" cy="3" r="2.5"/><path d="M4 8l8-2 3 5-3 1-1 7h-3l1-6-3 4-3-1 4-5z"/></svg>CONCEPT</h3>
      <ul><li>Closed Stance</li><li>Hand Postioning</li><li>Picture Frame Positioning</li><li>Point of Origin</li></ul>
    </section>
    <section class="group" style="left:322px;top:118px">
      <h3><svg viewBox="0 0 20 20"><circle cx="10" cy="3" r="2.5"/><path d="M3 9l7-3 7 3-1 2-4-1 2 9h-3l-1-5-2 5H5l2-9-3 1z"/></svg>OFFENSE</h3>
      <ul><li>Back Fist</li><li>Body Punch</li><li>Round Kick</li><li>Side Kick</li></ul>
    </section>
    <section class="group" style="left:24px;top:337px">
      <h3><svg viewBox="0 0 20 20"><path d="M1 5h18l-6 4 1 9-3-1-1-6-9-2z"/></svg>MOVEMENT</h3>
      <ul><li>Neutral Bounce</li></ul>
    </section>
    <section class="group" style="left:229px;top:337px">
      <h3><svg viewBox="0 0 20 20"><path d="M1 3l7 5h4l7-5-5 8-1 8H9l-1-8z"/></svg>DEFENCE &nbsp;/&nbsp; COUNTERS</h3>
      <ul style="padding-left:57px;margin-top:4px"><li>Wall Block</li><li>Push Checks</li></ul>
    </section>

    <div class="banner" style="top:492px">
      <svg viewBox="0 0 302 50" preserveAspectRatio="none"><polygon points="0,0 302,0 282,25 302,50 0,50 20,25" fill="var(--ribbon)"/><polyline points="22,6 280,6" stroke="var(--ribbon-edge)" stroke-dasharray="4 3" stroke-width="1.5"/><polyline points="22,44 280,44" stroke="#b98" stroke-dasharray="4 3" stroke-width="1.5"/></svg>
      <b>LEVEL TWO</b>
    </div>

    <section class="group" style="left:24px;top:617px">
      <h3><svg viewBox="0 0 20 20"><circle cx="12" cy="3" r="2.5"/><path d="M4 8l8-2 3 5-3 1-1 7h-3l1-6-3 4-3-1 4-5z"/></svg>CONCEPT</h3>
      <ul><li>Open Stance</li><li>Disturbing Rhythm</li><li>Technique Awareness</li></ul>
    </section>
    <section class="group ruled" style="left:326px;top:613px">
      <h3><svg viewBox="0 0 20 20"><path d="M1 5h18l-6 4 1 9-3-1-1-6-9-2z"/></svg>MOVEMENT</h3>
      <ul><li>Engage</li><li>Disengage</li><li>Fakes</li><li>Single</li><li>Double</li></ul>
    </section>
    <section class="group" style="left:29px;top:796px">
      <h3><svg viewBox="0 0 20 20"><circle cx="10" cy="3" r="2.5"/><path d="M3 9l7-3 7 3-1 2-4-1 2 9h-3l-1-5-2 5H5l2-9-3 1z"/></svg>OFFENSE</h3>
      <ul><li>Push Drag Back Fist Wall</li><li>Push Drag Body Punch Wall</li><li>Step Drag Roundhouse</li><li>Step Drag Side Kick</li></ul>
    </section>
    <section class="group ruled" style="left:52px;top:997px">
      <h3><svg viewBox="0 0 20 20"><path d="M1 3l7 5h4l7-5-5 8-1 8H9l-1-8z"/></svg>DEFENCE &nbsp;/&nbsp; COUNTERS</h3>
      <ul style="margin-left:6px"><li>Body Punch</li><li>Closed Stance</li><li>Push Check Body Punch</li></ul>
    </section>
  </main>
</div>
</body>
</html>
```